Lena Hartwell Web

Lena Hartwell is a singer/songwriter that has a presence in the market for over 20 years. She currently has a website, lenahartwell.example that needs a major makeover. IT needs to be reorganized to; 1) make it more user friendly; 2) enable multi-languages including; Spanish, French, Russian, Japanese, Chinese and Portuguese; 3) enable purchases online through a storefront of promotional merchandise and music tracks. She has a logo that needs an update, as well as we currently have a business card open on PixelBazaar for input. Working to re-brand, or refresh her brand.

Lena Hartwell is the next Rosa Delmont! She has 5 platinum records, Lumen Award nominations and tours with Harold Prescott globally and is Nora Vandermeer's key backup singer for 12 years.
Updates

Some common questions have come up.  Here is some further input:

1) Colors - No specific color in mind but probably earth tones.  Although at this point we''re completely open.  Mary likes classical style, Russian, French decor.  Paris architecture. Greek, Italian textures, Goddess like symbols from the Roman Empire, or the symbols and pomp of the British monarchy.  One name on tap for the new CD is "Lanterns Over Quiet Water"
2) Example website - I have not found a new one specifically, but what I don''t like about the existing one is it is not easy to navigate.  Needs to be streamlined and easy to navigate with a storefront for merchandise and music downloads.  
3) On Logo - We''re revamping a "Global" merchandise rollout logo.  We''ve also considered possibly modifying the old english "Hartwell" family crest which signifies royalty, but have not explored that too much.  The hexagon yellow logo on her current website, I was thinking of modifying to gold (brushed - or polished?), then taking the LH lettering using a fountain pen type look there the line thickness flows with pressure on the pen, then make the gold look like a pillow, with the letter making an impression into the gold pillow.  This expands to a high quality pin, blinged up broach with diamonds imbedded for example, Global label identity, tee shirts, label tag on fashion clothing etc etc. 
 4) One thing marketing has asked us to build is a routine video blog to reach out to fans in a personal way.  Short clips of daily activity, travel prep for shows, etc. Possibly a signup/fanpage where people get emails sent back whenever anything new is posted, like a video blog, new pics, new events.  A menu to choose what you get updates on. 

Thanks, Dennis

Target Market(s)

1) Fan base in Europe, Asia, Latin America and North America
2) Movie producers seeking soundtracks
3) Private clients seeking an outstanding performer for corporate events

Industry/Entity Type

Singer

Requirements
Must have
• Better organization into smaller pages. Items critical include: 1) music tracks, 2) ClipStream links, 3) photos & Video, 4) storefront to enable online merchandise purchase 5) a way to illustrate her genre from; gospel, to rock, funk, R&B, country,

```html
<!DOCTYPE html>
<html lang="en">
<head>
<meta charset="utf-8">
<title>Lena Hartwell — Home</title>
<link rel="stylesheet" href="https://fonts.googleapis.com/css2?family=Oswald:wght@400;500&family=Arimo:wght@400;700&family=PT+Sans:wght@400;700&display=swap">
<style>
:root{
  --bg-deep:#231008;
  --bg-brown:#3a1c0e;
  --ink:#222;
  --muted:#555;
  --red:#c8141b;
  --red-dark:#9c0f14;
  --rust:#8a3b12;
  --cream:#f6e6cf;
  --black:#0b0b0b;
  --nav:#1c1c1c;
  --footer:#1f1f1f;
  --gold:#c9a443;
  --white:#fff;
}
*{box-sizing:border-box;margin:0;padding:0}
html,body{width:1023px;height:1200px;overflow:hidden;background:var(--bg-deep)}
body{font-family:"Arimo",Arial,sans-serif;color:var(--ink)}
.stage{position:absolute;left:0;top:0;width:950px;height:1114px;transform:scale(1.07684);transform-origin:0 0;
  background:linear-gradient(90deg,#3d1d0d 0%,#2b1309 45%,#1f0d06 100%);overflow:hidden}
.abs{position:absolute}
.ph{position:absolute}
.backdrop-photo{left:0;top:90px;width:300px;height:1024px;
  background:radial-gradient(ellipse at 55% 45%,#d9c7ad 0%,#a8835c 30%,#5a3116 60%,transparent 80%)}
.backdrop-name{left:0;top:40px;font:300 110px "PT Sans",sans-serif;color:rgba(255,255,255,.05);white-space:nowrap}

/* header */
.brand{left:312px;top:12px;display:flex;align-items:center;gap:6px;font:500 17px "Oswald",sans-serif;color:var(--gold)}
.brand i{width:14px;height:14px;border-radius:50%;background:var(--gold);display:block}
.cart{left:766px;top:11px;font:8px "Arimo",sans-serif;color:#ddd;line-height:11px}
.cart b{color:#f2c200;font-weight:400}
.cart-icon{left:766px;top:12px}
.cart span{margin-left:21px;display:block}
.langs{left:530px;top:47px;display:flex;gap:14px;font:8px "Arimo",sans-serif;color:#eee}
.langs span{display:flex;align-items:center;gap:4px}
.langs i{width:9px;height:6px;display:block}
.search{left:728px;top:44px;width:137px;height:16px;background:#fff;font:7.5px "Arimo",sans-serif;color:#999;padding:4px 6px}

/* nav */
.nav{left:300px;top:75px;width:565px;height:25px;background:var(--nav);display:flex;align-items:center;padding-left:9px}
.nav a{font:400 11px "Oswald",sans-serif;color:#ddd;text-decoration:none;margin-right:17px;text-transform:uppercase}
.nav a.active{color:#e02a2a}
.nav-social{left:777px;top:82px;display:flex;gap:6px;align-items:center;font:500 7.5px "Oswald",sans-serif;color:#fff}
.nav-social i{width:9px;height:9px;display:block;border-radius:1px}

/* hero */
.hero{left:300px;top:100px;width:418px;height:196px;background:linear-gradient(120deg,#6c5a4c 0%,#a87a4e 35%,#3d2a20 60%,#7a6650 100%)}
.hero-title{left:333px;top:218px;background:rgba(0,0,0,.55);padding:0 4px;font:500 38px/44px "Oswald",sans-serif;color:#fff;letter-spacing:.5px}
.hero-sub{left:333px;top:262px;background:rgba(0,0,0,.7);padding:0 4px;font:400 12px/20px "Oswald",sans-serif;color:#aaa;text-transform:uppercase}
.genres{left:718px;top:100px;width:147px}
.genre{height:33px;padding:5px 10px;background:linear-gradient(#3b3b3b,#1e1e1e);border-bottom:1px solid #111}
.genre h4{font:400 9px "Oswald",sans-serif;color:#fff;text-transform:uppercase}
.genre p{font:7px "Arimo",sans-serif;color:#ccc;margin-top:1px}
.genre.active{background:linear-gradient(#fff,#dcdcdc)}
.genre.active h4{color:#222}.genre.active p{color:#444}

/* content sheet */
.sheet{left:300px;top:296px;width:565px;height:736px;background:var(--white)}
.tab{position:absolute;height:19px;background:var(--red);color:#fff;font:500 9.5px/19px "Oswald",sans-serif;text-align:center;letter-spacing:.5px}
.tab::after{content:"";position:absolute;right:0;bottom:-5px;border-top:5px solid var(--red-dark);border-right:7px solid transparent}

/* tracks */
.tracks{left:310px;top:326px;width:110px;height:686px;background:var(--cream)}
.track{position:absolute;left:10px;width:90px}
.cover{width:90px;height:72px;background:linear-gradient(150deg,#1d3a7a 0%,#4a8fd0 45%,#e8c230 70%,#1b2d5c 100%)}
.track h5{font:9px "Arimo",sans-serif;color:var(--rust);margin-top:15px}
.track p{font:7px/9.5px "Arimo",sans-serif;color:#333;margin-top:5px}
.track-rule{position:absolute;left:10px;width:90px;height:1px;background:#d8c5a8}
.more{left:320px;top:955px;width:90px;height:13px;background:linear-gradient(#f0a860,#d47a30);font:400 7.5px/13px "Oswald",sans-serif;color:#5a2208;text-align:center}

/* posts */
.posts{left:436px;top:307px;width:278px;height:448px;background:var(--black)}
.post{position:absolute;left:9px;width:260px}
.date{position:absolute;left:0;top:11px;width:27px;height:28px;background:#222;color:#fff;text-align:center;font:500 12px/13px "PT Sans",sans-serif;padding-top:3px}
.date small{display:block;font:7px "Arimo",sans-serif;color:#aaa}
.post h3{position:absolute;left:39px;top:10px;font:400 13.5px "PT Sans",sans-serif;color:var(--red);white-space:nowrap}
.meta{position:absolute;left:39px;top:28px;font:6.5px "Arimo",sans-serif;color:#ccc;white-space:nowrap}
.meta b{color:#e8b42c;font-weight:400}
.video{position:absolute;left:0;top:48px;width:260px;height:105px;background:linear-gradient(120deg,#2b2d6a 0%,#7c4e8a 45%,#c98262 60%,#2a2a55 100%)}
.play{position:absolute;left:111px;top:38px;width:36px;height:24px;border-radius:5px;background:rgba(0,0,0,.75)}
.play::after{content:"";position:absolute;left:14px;top:7px;border-left:9px solid #fff;border-top:5px solid transparent;border-bottom:5px solid transparent}
.controls{position:absolute;left:0;bottom:0;width:100%;height:20px;background:rgba(0,0,0,.6);font:6px "Arimo",sans-serif;color:#ddd;padding:9px 0 0 50px}
.post .body{position:absolute;left:0;top:161px;font:6.8px/9.5px "Arimo",sans-serif;color:#ddd}
.readmore{position:absolute;left:0;top:211px;font:6.5px "Arimo",sans-serif;color:#ddd;background:#1b1b1b;padding:2px 4px;border:1px solid #333}
.post-rule{left:436px;top:538px;width:278px;height:1px;background:#2c2c2c}
.pager{left:536px;top:737px;display:flex;gap:3px;font:6.5px/11px "Arimo",sans-serif;color:#ddd}
.pager span{border:1px solid #555;padding:0 3px;height:12px}
.pager .cur{border-color:#e8b42c;color:#e8b42c}

/* arrivals */
.arrivals-title{left:436px;top:770px;font:400 15px "Oswald",sans-serif;color:#1a1a1a;text-transform:uppercase}
.arrivals-sub{left:436px;top:791px;font:6.5px "Arimo",sans-serif;color:#666}
.album{position:absolute;width:91px}
.album .cover{width:91px;height:69px}
.album h6{font:7px "Arimo",sans-serif;color:#222;margin-top:5px;font-weight:400}
.album p{font:6.5px "Arimo",sans-serif;color:var(--red);margin-top:4px;display:flex;align-items:center;gap:4px}
.album p span{color:#666;display:flex;align-items:center;gap:3px}

/* right column */
.email{left:730px;top:331px;width:115px;height:16px;border:1px solid #ccc;font:7px/14px "Arimo",sans-serif;color:#777;padding-left:6px;background:#fafafa}
.email-go{left:830px;top:331px;width:15px;height:16px;background:#fff;border:1px solid #ccc}
.social{left:730px;top:354px;display:flex;gap:5px}
.social i{width:17px;height:17px;display:block;border-radius:2px}
.links{left:730px;top:413px;width:135px}
.links li{list-style:none;display:flex;gap:8px;height:16px;font:7px "Arimo",sans-serif;color:var(--rust)}
.links li b{width:9px;color:#333;font-weight:400;font-size:6px}
.promo{position:absolute;left:731px;width:125px;height:140px}
.promo h5{position:absolute;left:0;top:10px;width:100%;padding:2px 8px;background:rgba(0,0,0,.6);font:400 8.5px "Oswald",sans-serif;color:#fff;text-transform:uppercase}
.promo .deal{position:absolute;right:0;bottom:0;width:70px;height:80px;background:#c7301e;border-radius:60px 0 0 0;color:#fff;text-align:center;font:400 9px "PT Sans",sans-serif;padding-top:12px}
.promo .deal b{display:block;font:700 22px/22px "PT Sans",sans-serif}
.shot{position:absolute;left:731px;width:126px;height:62px}
.shot span{position:absolute;left:0;bottom:0;width:100%;height:15px;background:rgba(0,0,0,.8);font:500 6.5px/15px "Oswald",sans-serif;color:#fff;padding-left:7px}

/* footer */
.footer{left:300px;top:1032px;width:565px;height:82px;background:var(--footer)}
.f-name{left:330px;top:1046px;font:500 12px "Oswald",sans-serif;color:#fff}
.f-nav{left:441px;top:1049px;display:flex;gap:6px;font:400 8px "Oswald",sans-serif;color:#ddd}
.f-nav .active{color:#fff}
.f-lead{left:330px;top:1068px;width:90px;font:italic 6.5px/10px "Arimo",sans-serif;color:#888}
.f-box{position:absolute;top:1070px;height:36px;background:#0f0f0f}
.f-label{position:absolute;top:1070px;height:11px;background:#111;font:500 6.5px/11px "Oswald",sans-serif;color:#fff;padding:0 4px}
.f-text{left:450px;top:1086px;font:italic 6.5px "Arimo",sans-serif;color:#999}
.follow{left:648px;top:1090px;display:flex;gap:7px;align-items:center;font:6.5px "Arimo",sans-serif;color:#ccc}
.follow span{display:flex;gap:3px;align-items:center}
.follow i{width:9px;height:9px;display:block;border-radius:1px}
</style>
</head>
<body>
<div class="stage">
  <div class="ph backdrop-photo" role="img" aria-label="Photo of the singer in a white halter gown"></div>
  <div class="abs backdrop-name">Lena Hartwell</div>

  <header>
    <div class="abs brand"><i></i>Lena Hartwell</div>
    <svg class="abs cart-icon" width="18" height="14" viewBox="0 0 18 14" aria-hidden="true"><path d="M1 1h3l2 8h9l2-6H5" fill="none" stroke="#fff" stroke-width="1.3"/><circle cx="7" cy="12" r="1.3" fill="#fff"/><circle cx="14" cy="12" r="1.3" fill="#fff"/></svg>
    <div class="abs cart"><span>Total <b>5 items</b> in your cart</span><span>Viewcart | Checkout</span></div>
    <div class="abs langs">
      <span><i style="background:linear-gradient(#c8102e,#fff,#012169)"></i>English</span>
      <span><i style="background:linear-gradient(#c60b1e 25%,#ffc400 25% 75%,#c60b1e 75%)"></i>Spanish</span>
      <span><i style="background:linear-gradient(90deg,#0055a4 33%,#fff 33% 66%,#ef4135 66%)"></i>French</span>
      <span><i style="background:linear-gradient(#fff 33%,#0039a6 33% 66%,#d52b1e 66%)"></i>Russian</span>
    </div>
    <div class="abs search">What are you looking for?</div>
    <svg class="abs" style="left:851px;top:47px" width="9" height="9" viewBox="0 0 9 9" aria-hidden="true"><circle cx="3.7" cy="3.7" r="2.7" fill="none" stroke="#999"/><path d="M5.8 5.8L8.5 8.5" stroke="#999"/></svg>
  </header>

  <nav class="abs nav">
    <a class="active">Home</a><a>Events</a><a>Music</a><a>Video</a><a>Pictures</a><a>About</a><a>Discography</a><a>Contact</a>
  </nav>
  <div class="abs nav-social"><i style="background:#4aa3d8"></i><i style="background:#3b5a98"></i><i style="background:#e8801c"></i>SUBSCRIBE</div>

  <section>
    <div class="ph hero" role="img" aria-label="Portrait of the singer seated in a tan leather car seat"></div>
    <div class="abs hero-title">LENA HARTWELL</div>
    <div class="abs hero-sub">Lanterns Over Quiet Water</div>
    <div class="abs genres">
      <div class="genre active"><h4>Her Picture</h4><p>Lorem ipsim dolor sit amet</p></div>
      <div class="genre"><h4>Gospel</h4><p>Lorem ipsim dolor sit amet</p></div>
      <div class="genre"><h4>Rock</h4><p>Lorem ipsim dolor sit amet</p></div>
      <div class="genre"><h4>Funk</h4><p>Lorem ipsim dolor sit amet</p></div>
      <div class="genre"><h4>R&amp;B</h4><p>Lorem ipsim dolor sit amet</p></div>
      <div class="genre"><h4>Country</h4><p>Lorem ipsim dolor sit amet</p></div>
    </div>
  </section>

  <main>
    <div class="abs sheet"></div>

    <aside>
      <div class="abs tracks">
        <div class="track" style="top:14px"><div class="cover" role="img" aria-label="Album cover art"></div><h5>Lorem Ipsum Dolor</h5><p>Lorem ipsum dolor sit amet, consectetuer adipiscing elit. Morbi pretium feugiat mauris.</p></div>
        <div class="track-rule" style="top:156px"></div>
        <div class="track" style="top:167px"><div class="cover" role="img" aria-label="Album cover art"></div><h5>Lorem Ipsum Dolor</h5><p>Lorem ipsum dolor sit amet, consectetuer adipiscing elit. Morbi pretium feugiat mauris.</p></div>
        <div class="track-rule" style="top:309px"></div>
        <div class="track" style="top:320px"><div class="cover" role="img" aria-label="Album cover art"></div><h5>Lorem Ipsum Dolor</h5><p>Lorem ipsum dolor sit amet, consectetuer adipiscing elit. Morbi pretium feugiat mauris.</p></div>
        <div class="track-rule" style="top:463px"></div>
        <div class="track" style="top:474px"><div class="cover" role="img" aria-label="Album cover art"></div><h5>Lorem Ipsum Dolor</h5><p>Lorem ipsum dolor sit amet, consectetuer adipiscing elit. Morbi pretium feugiat mauris.</p></div>
        <div class="track-rule" style="top:616px"></div>
      </div>
      <div class="tab" style="left:292px;top:308px;width:136px">MUSIC TRACKS</div>
      <div class="abs more">MORE TRACKS ˅</div>
    </aside>

    <section>
      <div class="abs posts">
        <article class="post" style="top:0">
          <div class="date">02<small>Sept</small></div>
          <h3>Sunshine music by Lena Hartwell</h3>
          <div class="meta">Posted by <b>Lena</b> &nbsp;|&nbsp; 157 Comments</div>
          <div class="video" role="img" aria-label="Concert video still of the singer at a microphone"><div class="play"></div><div class="controls">0:00 / 5:04</div></div>
          <p class="body">Lorem ipsum dolor sit amet, consectetuer adipiscing elit. Morbi pretium feugiat mauris. In hac habitasse platea dictumst. Morbi commodo, massa nec suscipit vulputate, nisi mauris suscipit mauris, sagittis ultrices lorem ante vitae nisl. Nam pharetra vehicula massa. Cras blandit nulla eu nisl.</p>
          <span class="readmore">Read the full story »</span>
        </article>
        <article class="post" style="top:233px">
          <div class="date">02<small>Sept</small></div>
          <h3>Sunshine music by Lena Hartwell</h3>
          <div class="meta">Posted by <b>Lena</b> &nbsp;|&nbsp; 157 Comments</div>
          <div class="video" style="height:66px" role="img" aria-label="Concert photo of the singer with arms raised"><div class="play" style="top:22px"></div></div>
          <p class="body" style="top:124px">Lorem ipsum dolor sit amet, consectetuer adipiscing elit. Morbi pretium feugiat mauris. In hac habitasse platea dictumst. Morbi commodo, massa nec suscipit vulputate, nisi mauris suscipit mauris, sagittis ultrices lorem ante vitae nisl. Nam pharetra vehicula massa. Cras blandit nulla eu nisl.</p>
          <span class="readmore" style="top:173px">Read the full story »</span>
        </article>
      </div>
      <div class="abs post-rule"></div>
      <div class="abs post-rule" style="top:732px"></div>
      <div class="abs pager"><span>Page 1 of 2</span><span class="cur">1</span><span>2</span><span>»</span></div>

      <h2 class="abs arrivals-title">Latest Arrivals</h2>
      <p class="abs arrivals-sub">Check our all latest Albums in this section.</p>
      <div class="album" style="left:436px;top:813px"><div class="cover" role="img" aria-label="Album cover art"></div><h6>Title of the Album</h6><p>$179.00 | <span>🛒 Add to Cart</span></p></div>
      <div class="album" style="left:531px;top:813px"><div class="cover" role="img" aria-label="Album cover art"></div><h6>Title of the Album</h6><p>$179.00 | <span>🛒 Add to Cart</span></p></div>
      <div class="album" style="left:625px;top:813px"><div class="cover" role="img" aria-label="Album cover art"></div><h6>Title of the Album</h6><p>$179.00 | <span>🛒 Add to Cart</span></p></div>
      <div class="album" style="left:436px;top:920px"><div class="cover" role="img" aria-label="Album cover art"></div><h6>Title of the Album</h6><p>$179.00 | <span>🛒 Add to Cart</span></p></div>
      <div class="album" style="left:531px;top:920px"><div class="cover" role="img" aria-label="Album cover art"></div><h6>Title of the Album</h6><p>$179.00 | <span>🛒 Add to Cart</span></p></div>
      <div class="album" style="left:625px;top:920px"><div class="cover" role="img" aria-label="Album cover art"></div><h6>Title of the Album</h6><p>$179.00 | <span>🛒 Add to Cart</span></p></div>
    </section>

    <aside>
      <div class="tab" style="left:730px;top:308px;width:142px">SUBSCRIBE</div>
      <div class="abs email">fan@lenahartwell.example</div>
      <div class="abs email-go"><svg width="13" height="14" viewBox="0 0 13 14" aria-hidden="true"><rect x="3" y="4" width="8" height="6" fill="none" stroke="#c8141b"/><path d="M3 4l4 3 4-3" fill="none" stroke="#c8141b"/></svg></div>
      <div class="abs social"><i style="background:#3b5a98"></i><i style="background:#4aa3d8"></i><i style="background:#e8801c"></i></div>

      <div class="tab" style="left:730px;top:383px;width:142px">CLIPSTREAM LINKS</div>
      <ul class="abs links">
        <li><b>34</b>Interview with Ines Calloway</li>
        <li><b>67</b>Top summer discounts in Paris</li>
        <li><b>47</b>Victor Ashdown Exhibit</li>
        <li><b>3</b>Best runaway shows in Moscow</li>
        <li><b>43</b>Interview with Ines Calloway</li>
        <li><b>27</b>Top summer discounts in Paris</li>
        <li><b>79</b>Victor Ashdown Exhibit</li>
        <li><b>3</b>Best runaway shows in Moscow</li>
      </ul>

      <div class="promo" style="top:549px;background:linear-gradient(160deg,#3a2a18,#b78a3e 50%,#5a3b1c)" role="img" aria-label="Promo photo of the singer in a red dress">
        <h5>Cool Collections</h5><div class="deal">Get Winter<b>50%</b>off</div>
      </div>
      <div class="promo" style="top:698px;background:linear-gradient(160deg,#20163a,#6a3b7a 50%,#1b1430)" role="img" aria-label="Promo photo of the singer on stage">
        <h5>Cool Collections</h5><div class="deal">Get Winter<b>50%</b>off</div>
      </div>

      <div class="tab" style="left:730px;top:850px;width:142px">LATEST PHOTOS</div>
      <div class="shot" style="top:879px;background:linear-gradient(120deg,#2a1a14,#8a5a3a 50%,#2a1a14)" role="img" aria-label="Stage photo of two performers"><span>PHOTO TITLE</span></div>
      <div class="shot" style="top:948px;background:linear-gradient(120deg,#1d140f,#7a5030 50%,#241810)" role="img" aria-label="Photo of the band performing"><span>PHOTO TITLE</span></div>
    </aside>
  </main>

  <footer>
    <div class="abs footer"></div>
    <div class="abs f-name">LENA HARTWELL</div>
    <div class="abs f-nav"><span class="active">HOME</span><span>EVENTS</span><span>MUSIC</span><span>VIDEO</span><span>PICTURES</span><span>ABOUT</span><span>CONTACT</span></div>
    <p class="abs f-lead">LOREM IPUM DOLOR SIT AMET</p>
    <div class="f-box" style="left:442px;width:175px"></div>
    <div class="f-label" style="left:446px">ABOUT HER</div>
    <p class="abs f-text">LOREM IPUM DOLOR SIT AMET</p>
    <div class="f-box" style="left:640px;width:175px"></div>
    <div class="f-label" style="left:640px">SUBSCRIBE</div>
    <div class="abs follow">Follow us: <span><i style="background:#4aa3d8"></i>Chirpline</span><span><i style="background:#3b5a98"></i>Friendbook</span><span><i style="background:#e8801c"></i>RSS</span></div>
  </footer>
</div>
</body>
</html>
```